The Driftwood Caster----- Wade Pellman----- Kellow Creek Bronzeback ------www.thedriftwoodcaster.test-----

Hello Fishermen,
The Umpqua rivers peaceful beauty is like no other river, the private Hollis section offers trophy bass fishing along with 100 fish days. Spin cast or fly fish for bass. This 8 hour fishing trip takes you into a remote section of ranches and wilderness abundant with not only thousands of bass per mile...... but wildlife and scenery are breath taking in this quite section of river.
This trip is for everyone, easy for the Grand Parents and the grand kids...... Women love this trip with the warm weather and easy fishing.
So Let's go Fishing...... please call or email us today and book your trip or with any questions you have.
Vacation Rentals, Motels and R.V parks all available close by.

Email us at: driftwoodcaster@mailbrook.test
Visit our website at: www.thedriftwoodcaster.test
Call us at: 541-555-0148

Thank you for fishing with us,
Wade Pellman

return address;
Wade Pellman
p.o. box 712
Elkton, Oregon 97521

****NOTE for front of post card layout person should go to our website home page for ideas, and photos. Please feel free to change our message above to correct grammar and make read smoother, Thank you.....

there is no contest....not sure how that got there...

```html
<!DOCTYPE html>
<html lang="en">
<head>
<meta charset="utf-8">
<title>The Driftwood Caster – Postcard</title>
<link href="https://fonts.googleapis.com/css2?family=Mountains+of+Christmas:wght@400;700&family=Bree+Serif&family=Arimo:ital,wght@0,400;1,700&display=swap" rel="stylesheet">
<style>
  :root {
    --page: #ffffff;
    --card-back: #eef0f8;
    --ink: #222428;
    --teal: #1f9aa6;
    --white: #ffffff;
    --pennant: rgba(30, 34, 40, 0.55);
    --bass-green: #c9dc8a;
    --bass-outline: #2f3a1c;
    --rule: #c4c6cc;
  }
  * { box-sizing: border-box; margin: 0; padding: 0; }
  html, body { width: 771px; height: 1200px; overflow: hidden; background: var(--page); }
  .postcard {
    position: absolute;
    left: 29px;
    width: 713px;
    overflow: hidden;
  }
  /* Front */
  .front { top: 29px; height: 562px; }
  .front-photo {
    position: absolute; inset: 0;
    background:
      linear-gradient(180deg, #6d6a2c 0%, #a99632 22%, #c2a945 40%, #556a78 58%, #2f5d9a 72%, #4a78c4 86%, #6d93d6 100%);
  }
  .pennant { position: absolute; left: 0; top: 0; }
  .front-header {
    position: absolute; left: 30px; width: 396px; top: 0; height: 360px;
    text-align: center; color: var(--white);
    font-family: "Mountains of Christmas", serif; font-weight: 700;
  }
  .front-header > div {
    position: absolute; left: -20px; right: -20px;
    white-space: nowrap; line-height: 1;
  }
  .brand { top: 52px; font-size: 40px; letter-spacing: 0; }
  .guide-name { top: 126px; font-size: 32px; }
  .guide-role { top: 182px; font-size: 27px; font-weight: 400; }
  .phone-big { top: 238px; font-size: 40px; }
  .site-big { top: 302px; font-size: 23px; }
  .trip-offer {
    position: absolute; left: 20px; width: 420px; top: 378px;
    text-align: center; white-space: nowrap;
    font-family: "Bree Serif", serif;
    font-size: 30px; line-height: 46px;
    color: var(--bass-green);
    -webkit-text-stroke: 1px var(--bass-outline);
    text-shadow: 1px 2px 2px rgba(0,0,0,0.5);
  }
  /* Back */
  .back { top: 617px; height: 552px; background: var(--card-back); }
  .back-photo {
    position: absolute; left: 2px; top: 0; width: 352px; height: 130px;
    background: linear-gradient(180deg, #b9d3ee 0%, #6d8a5c 30%, #2f4f2e 52%, #4d6f8c 72%, #7d8f5a 100%);
  }
  .message {
    position: absolute; left: 28px; top: 145px; width: 300px;
    font-family: "Arimo", sans-serif; font-size: 13.4px; line-height: 19px;
    color: var(--ink); letter-spacing: -0.45px;
  }
  .message .call-to-action { color: var(--teal); }
  .signoff {
    position: absolute; left: 93px; top: 432px;
    font-family: "Arimo", sans-serif; font-style: italic; font-weight: 700;
    font-size: 13.5px; line-height: 19px; color: var(--ink);
  }
  .contact-list {
    position: absolute; left: 93px; top: 474px; list-style: none;
    font-family: "Arimo", sans-serif; color: var(--teal);
  }
  .contact-list li { display: flex; align-items: center; gap: 8px; height: 19px; white-space: nowrap; }
  .contact-list .phones { font-size: 13.5px; }
  .contact-list .small-caps { font-size: 11px; text-transform: uppercase; }
  .contact-list svg { width: 12px; height: 12px; flex: none; }
  .stamp-box {
    position: absolute; left: 580px; top: 27px; width: 122px; height: 127px;
    border: 2px dashed var(--rule);
  }
  .address-line {
    position: absolute; left: 379px; width: 323px; height: 0;
    border-top: 2px dashed var(--rule);
  }
</style>
</head>
<body>

<section class="postcard front">
  <div class="front-photo" role="img" aria-label="Photo of an angler fly casting from dark riverside rocks, golden autumn trees reflected in the water"></div>
  <svg class="pennant" width="713" height="562" viewBox="0 0 713 562" aria-hidden="true">
    <polygon points="30,0 426,0 426,318 229,396 30,318" fill="var(--pennant)"/>
  </svg>
  <div class="front-header">
    <div class="brand">THE DRIFTWOOD CASTER</div>
    <div class="guide-name">WADE PELLMAN</div>
    <div class="guide-role">Fishing Guide &amp; Outfitter</div>
    <div class="phone-big">1-800-555-0172</div>
    <div class="site-big">THEDRIFTWOODCASTER.TEST</div>
  </div>
  <div class="trip-offer">
    Bronzeback Bass<br>
    One day guided fishing trips on<br>
    the Kellow Creek Private Hollis
  </div>
</section>

<section class="postcard back">
  <div class="back-photo" role="img" aria-label="Panorama of a winding river bend with forested hills and a blue sky"></div>
  <p class="message">
    Kellow Creek's peaceful beauty is like no other river, the private Hollis section offers trophy bass fishing along with 100 fish days. Spin cast or fly fish for bass. This 8 hour fishing trip takes you into a remote section of ranches and wilderness abundant with not only thousands of bass per mile...... but wildlife and scenery are breathtaking in this quiet section of river. This trip is for everyone, easy for the Grand Parents and the grand kids...... Women love this trip with the warm weather and easy fishing. Vacation Rentals, Motels and R.V parks all available close by. <span class="call-to-action">So Let's go Fishing...... please call or email us today and book your trip or with any questions you have.</span>
  </p>
  <div class="signoff">Thank you for fishing with us!<br>Wade Pellman</div>
  <ul class="contact-list">
    <li class="phones">
      <svg viewBox="0 0 12 12" aria-hidden="true"><circle cx="6" cy="6" r="5.2" fill="none" stroke="currentColor" stroke-width="1"/><path d="M4 3.2c-.6.4-.7 1.4 0 2.6s1.8 2.2 2.8 2.4c.6.1 1-.2 1.2-.6l-1-.9-.7.4c-.5-.2-1.3-1-1.5-1.6l.4-.7z" fill="currentColor"/></svg>
      541-555-0148 or&nbsp; 800-555-0172
    </li>
    <li class="small-caps">
      <svg viewBox="0 0 12 12" aria-hidden="true"><rect x="1" y="2.5" width="10" height="7" fill="none" stroke="currentColor" stroke-width="1"/><path d="M1 2.5l5 4 5-4" fill="none" stroke="currentColor" stroke-width="1"/></svg>
      driftwoodcaster@mailbrook.test
    </li>
    <li class="small-caps">
      <svg viewBox="0 0 12 12" aria-hidden="true"><circle cx="6" cy="6" r="5.2" fill="none" stroke="currentColor" stroke-width="1"/><rect x="5.4" y="5" width="1.2" height="4" fill="currentColor"/><circle cx="6" cy="3.3" r=".75" fill="currentColor"/></svg>
      www.thedriftwoodcaster.test
    </li>
  </ul>
  <div class="stamp-box" aria-label="Stamp area"></div>
  <div class="address-line" style="top:278px"></div>
  <div class="address-line" style="top:345px"></div>
  <div class="address-line" style="top:412px"></div>
</section>

</body>
</html>
```